Resume

I am an industrial designer that has just graduated from school. I have been trying to brand myself when applying to companies. Even though I know of the basic principles in graphic design I have difficulty executing it. I have supplied my logo (which is simple but clean) and two forms of my resume I was playing around with. One is Mostly text the other has more color and is more graphic. I would like something in the middle. I would like to have a creative graph that is easy to read that displays my skills.
Updates

Project Deadline Extended
Reason: Some of the designers were asking for an extra day. I gave it 3.

Industry/Entity Type

Graphic Design

```html
<!DOCTYPE html>
<html lang="en">
<head>
<meta charset="utf-8">
<title>Owen Castell — Resume</title>
<link rel="stylesheet" href="https://fonts.googleapis.com/css2?family=Bebas+Neue&display=swap">
<style>
  :root {
    --brand-red: #b03226;
    --text-grey: #7a7a7a;
    --skill-grey: #a3a3a3;
    --star-off: #9a9a9a;
    --paper: #ffffff;
    --shadow: rgba(0, 0, 0, 0.55);
  }
  * { margin: 0; padding: 0; box-sizing: border-box; }
  html, body { width: 927px; height: 1200px; overflow: hidden; background: var(--paper); }
  body { font-family: "Bebas Neue", "Oswald", sans-serif; }
  .resume { position: relative; width: 927px; height: 1200px; background: var(--paper); }

  /* identity block */
  .identity-card { position: absolute; left: 57px; top: 50px; width: 266px; height: 361px; }
  .identity-mark {
    position: absolute; left: 0; top: 0; width: 266px; height: 212px;
    background: var(--brand-red); border-radius: 44px 44px 0 44px;
    display: flex; align-items: center; justify-content: center;
    color: var(--paper); font-size: 38px; letter-spacing: 1px;
  }
  .photo-slot {
    position: absolute; left: 0; top: 212px; width: 266px; height: 149px;
    border: 1px solid #222; border-top: none; border-radius: 0 0 0 34px;
    display: flex; align-items: center; justify-content: center;
    color: var(--brand-red); font-size: 26px; padding-bottom: 20px;
  }

  /* contact + name */
  .contact { position: absolute; left: 393px; top: 42px; color: var(--brand-red); font-size: 42px; line-height: 50px; }
  .name { position: absolute; left: 393px; top: 208px; color: var(--brand-red); font-size: 64px; line-height: 1; letter-spacing: 1px; font-weight: 400; }
  .about { position: absolute; left: 395px; top: 291px; font-size: 26px; line-height: 32px; color: var(--text-grey); }
  .about h2, .timeline h3 { color: var(--brand-red); font-weight: 400; font-size: 26px; }

  /* timeline */
  .timeline { position: absolute; left: 60px; top: 447px; width: 268px; font-size: 26px; line-height: 32px; color: var(--text-grey); }
  .timeline-entry { margin-bottom: 24px; }

  /* skills panel */
  .skills-panel {
    position: absolute; left: 395px; top: 451px; width: 440px; height: 667px;
    background: var(--brand-red); border-radius: 0 50px 34px 42px;
    box-shadow: 9px 9px 8px var(--shadow);
    padding: 60px 0 0 48px;
  }
  .skills-panel h2 { color: var(--paper); font-weight: 400; font-size: 26px; line-height: 32px; margin-bottom: 30px; }
  .skill-group + .skill-group { margin-top: 32px; }
  .skill-row { display: flex; align-items: center; height: 32px; }
  .skill-name { width: 225px; color: var(--skill-grey); font-size: 26px; }
  .rating { width: 137px; height: 27px; display: block; }
  .star-on { fill: var(--paper); }
  .star-off { fill: var(--star-off); }
</style>
</head>
<body>
<svg width="0" height="0" style="position:absolute" aria-hidden="true">
  <defs>
    <path id="star-shape" d="M12 1.2l3.2 6.7 7.4.9-5.4 5.1 1.4 7.3L12 17.6l-6.6 3.6 1.4-7.3L1.4 8.8l7.4-.9z"/>
    <clipPath id="left-half" clipPathUnits="userSpaceOnUse"><rect x="0" y="0" width="12" height="24"/></clipPath>
    <symbol id="star-full" viewBox="0 0 24 24"><use href="#star-shape" class="star-on"/></symbol>
    <symbol id="star-empty" viewBox="0 0 24 24"><use href="#star-shape" class="star-off"/></symbol>
    <symbol id="star-half" viewBox="0 0 24 24">
      <use href="#star-shape" class="star-off"/>
      <use href="#star-shape" class="star-on" clip-path="url(#left-half)"/>
    </symbol>
  </defs>
</svg>

<main class="resume">
  <div class="identity-card">
    <div class="identity-mark">Owen Castell</div>
    <div class="photo-slot" role="img" aria-label="Portrait photo of the designer goes here">YOUR PHOTO HERE</div>
  </div>

  <div class="contact">
    <p>1.555.204.3187</p>
    <p>DILIGENTOWEN@MAILBOX.COM</p>
    <p>FOLIOBOARD.NET/OCASTELL</p>
  </div>
  <h1 class="name">OWEN CASTELL</h1>

  <section class="about">
    <h2>ABOUT MYSELF</h2>
    <p>BORN 14.07.1989</p>
    <p>IN OREGON, USA</p>
    <p>MAJOR IN INDUSTRIAL DESIGN</p>
  </section>

  <section class="timeline">
    <div class="timeline-entry"><h3>CORAL BAY STATE COLLEGE<br>JUNE 2009</h3><p>DRAFTING DESIGN</p></div>
    <div class="timeline-entry"><h3>INTERNSHIP<br>2014</h3><p>CREATED ADVERTISEMENTS<br>AND BANNERS FOR A COFFEE<br>ROASTER</p></div>
    <div class="timeline-entry"><h3>FREELANCE DESIGNER<br>2014 - 2015</h3><p>DESIGNED AND BUILT<br>INFORMATION BOOTH FOR A<br>COMMUNITY CENTER<br>SERVING OVER<br>3,000 MEMBERS</p></div>
    <div class="timeline-entry"><h3>HARBOR CITY COLLEGE OF ART<br>AND DESIGN<br>MAY 2015</h3><p>INDUSTRIAL DESIGN BFA</p></div>
  </section>

  <section class="skills-panel">
    <div class="skill-group">
      <h2>TECHNICAL SKILLS</h2>
      <div class="skill-row"><span class="skill-name">SOLIDFORGE</span><svg class="rating" viewBox="0 0 137 27" aria-label="4 of 5"><use href="#star-full" x="0" width="27" height="27"/><use href="#star-full" x="27" width="27" height="27"/><use href="#star-full" x="54" width="27" height="27"/><use href="#star-full" x="81" width="27" height="27"/><use href="#star-empty" x="108" width="27" height="27"/></svg></div>
      <div class="skill-row"><span class="skill-name">CURVEWORKS 3D</span><svg class="rating" viewBox="0 0 137 27" aria-label="4 of 5"><use href="#star-full" x="0" width="27" height="27"/><use href="#star-full" x="27" width="27" height="27"/><use href="#star-full" x="54" width="27" height="27"/><use href="#star-full" x="81" width="27" height="27"/><use href="#star-empty" x="108" width="27" height="27"/></svg></div>
      <div class="skill-row"><span class="skill-name">LUMASHOT</span><svg class="rating" viewBox="0 0 137 27" aria-label="4.5 of 5"><use href="#star-full" x="0" width="27" height="27"/><use href="#star-full" x="27" width="27" height="27"/><use href="#star-full" x="54" width="27" height="27"/><use href="#star-full" x="81" width="27" height="27"/><use href="#star-half" x="108" width="27" height="27"/></svg></div>
      <div class="skill-row"><span class="skill-name">SHOP SKILLS</span><svg class="rating" viewBox="0 0 137 27" aria-label="4.5 of 5"><use href="#star-full" x="0" width="27" height="27"/><use href="#star-full" x="27" width="27" height="27"/><use href="#star-full" x="54" width="27" height="27"/><use href="#star-full" x="81" width="27" height="27"/><use href="#star-half" x="108" width="27" height="27"/></svg></div>
      <div class="skill-row"><span class="skill-name">PIXELSHOP</span><svg class="rating" viewBox="0 0 137 27" aria-label="5 of 5"><use href="#star-full" x="0" width="27" height="27"/><use href="#star-full" x="27" width="27" height="27"/><use href="#star-full" x="54" width="27" height="27"/><use href="#star-full" x="81" width="27" height="27"/><use href="#star-full" x="108" width="27" height="27"/></svg></div>
      <div class="skill-row"><span class="skill-name">PAGESET</span><svg class="rating" viewBox="0 0 137 27" aria-label="3.5 of 5"><use href="#star-full" x="0" width="27" height="27"/><use href="#star-full" x="27" width="27" height="27"/><use href="#star-full" x="54" width="27" height="27"/><use href="#star-half" x="81" width="27" height="27"/><use href="#star-empty" x="108" width="27" height="27"/></svg></div>
      <div class="skill-row"><span class="skill-name">VECTORA</span><svg class="rating" viewBox="0 0 137 27" aria-label="2.5 of 5"><use href="#star-full" x="0" width="27" height="27"/><use href="#star-full" x="27" width="27" height="27"/><use href="#star-half" x="54" width="27" height="27"/><use href="#star-empty" x="81" width="27" height="27"/><use href="#star-empty" x="108" width="27" height="27"/></svg></div>
    </div>
    <div class="skill-group">
      <h2>PERSONAL SKILLS</h2>
      <div class="skill-row"><span class="skill-name">PROFESSIONALISM</span><svg class="rating" viewBox="0 0 137 27" aria-label="4 of 5"><use href="#star-full" x="0" width="27" height="27"/><use href="#star-full" x="27" width="27" height="27"/><use href="#star-full" x="54" width="27" height="27"/><use href="#star-full" x="81" width="27" height="27"/><use href="#star-empty" x="108" width="27" height="27"/></svg></div>
      <div class="skill-row"><span class="skill-name">ORGANIZATION</span><svg class="rating" viewBox="0 0 137 27" aria-label="5 of 5"><use href="#star-full" x="0" width="27" height="27"/><use href="#star-full" x="27" width="27" height="27"/><use href="#star-full" x="54" width="27" height="27"/><use href="#star-full" x="81" width="27" height="27"/><use href="#star-full" x="108" width="27" height="27"/></svg></div>
      <div class="skill-row"><span class="skill-name">CREATIVITY</span><svg class="rating" viewBox="0 0 137 27" aria-label="5 of 5"><use href="#star-full" x="0" width="27" height="27"/><use href="#star-full" x="27" width="27" height="27"/><use href="#star-full" x="54" width="27" height="27"/><use href="#star-full" x="81" width="27" height="27"/><use href="#star-full" x="108" width="27" height="27"/></svg></div>
      <div class="skill-row"><span class="skill-name">COMMUNICATION</span><svg class="rating" viewBox="0 0 137 27" aria-label="4 of 5"><use href="#star-full" x="0" width="27" height="27"/><use href="#star-full" x="27" width="27" height="27"/><use href="#star-full" x="54" width="27" height="27"/><use href="#star-full" x="81" width="27" height="27"/><use href="#star-empty" x="108" width="27" height="27"/></svg></div>
      <div class="skill-row"><span class="skill-name">TEAMWORK</span><svg class="rating" viewBox="0 0 137 27" aria-label="5 of 5"><use href="#star-full" x="0" width="27" height="27"/><use href="#star-full" x="27" width="27" height="27"/><use href="#star-full" x="54" width="27" height="27"/><use href="#star-full" x="81" width="27" height="27"/><use href="#star-full" x="108" width="27" height="27"/></svg></div>
    </div>
  </section>
</main>
</body>
</html>
```